Keystone Allies Website

My business has been word of mouth over the last 3 years and has grown. Now I need a website for additional marketing as we have new clients asking for a website.

You have already completed my Logo during an earlier project. I have attached the logo.

We do Staff Augmentation and Operation Support.

What is that?
Staff augmentation is an outsourcing strategy that allows companies to fill specific, temporary roles to achieve business objectives. This staffing method complements existing teams with specific talent, enhancing business capabilities or filling gaps left by members on extended leave.

We work alongside the internal recruiting team to assist clients to meet and exceed financial goals.

```html
<!DOCTYPE html>
<html lang="en">
<head>
<meta charset="utf-8">
<title>Keystone Allies — Staff Augmentation and Operation Support</title>
<link href="https://fonts.googleapis.com/css2?family=Montserrat:wght@400;500;600;700;800&display=swap" rel="stylesheet">
<style>
:root{
  --navy:#252b42;
  --navy-deep:#1f2544;
  --muted:#737373;
  --orange:#ff7b3e;
  --teal:#125e67;
  --line:#e6e6e6;
  --soft:#fafafa;
  --white:#ffffff;
}
*{box-sizing:border-box;margin:0;padding:0}
html,body{width:1200px;height:3895px;overflow:hidden}
body{font-family:"Montserrat",sans-serif;color:var(--navy);background:var(--white);position:relative}
.abs{position:absolute}
.center{text-align:center;left:0;width:1200px}
.section-title{font-size:32px;font-weight:700;letter-spacing:.2px}
.section-sub{font-size:12px;color:var(--muted);line-height:17px}

/* header + hero */
.hero{position:absolute;left:0;top:0;width:1200px;height:660px;background:linear-gradient(90deg,#f4f5f5 0%,#f1f2f2 45%,#e9edee 100%)}
.hero-photo{position:absolute;left:560px;top:0;width:640px;height:660px;background:radial-gradient(ellipse at 70% 40%,#c9a98f 0%,#9fb3c0 35%,#d5dde2 70%,rgba(241,242,242,0) 100%)}
.brand{position:absolute;left:163px;top:27px;display:flex;align-items:center;gap:8px}
.brand-mark{width:28px;height:28px;border-radius:50%;background:var(--teal)}
.brand-name{font-size:15px;font-weight:700;color:var(--teal);letter-spacing:.3px}
.nav{position:absolute;left:348px;top:35px;display:flex;gap:19px;font-size:12px;font-weight:500;color:var(--muted)}
.menu-toggle{position:absolute;left:1131px;top:35px}
.hero-title{position:absolute;left:163px;top:153px;font-size:52px;line-height:66px;font-weight:800;color:var(--navy)}
.hero-text{position:absolute;left:163px;top:376px;font-size:18px;line-height:25px;color:var(--muted)}
.btn{display:flex;align-items:center;justify-content:center;border-radius:30px;font-size:12px;font-weight:700}
.btn-primary{background:var(--orange);color:var(--white)}
.btn-ghost{border:1.5px solid var(--teal);color:var(--teal)}

.service{position:absolute;top:609px;width:274px;height:201px;background:var(--white);padding:33px 33px 0;box-shadow:0 10px 30px rgba(0,0,0,.04)}
.service h3{font-size:20px;line-height:27px;font-weight:700;margin-top:20px}
.service p{font-size:12px;line-height:17px;color:var(--muted);margin-top:13px}
.service.featured{background:var(--teal);color:var(--white)}
.service.featured p{color:#e8f1f2}

.stat{position:absolute;top:1008px;width:192px;height:172px;background:var(--white);box-shadow:0 6px 20px rgba(0,0,0,.05);text-align:center;padding-top:27px}
.stat-num{font-size:31px;font-weight:700;margin-top:14px}
.stat-label{font-size:12px;font-weight:700;color:var(--muted);margin-top:12px}

.advice-band{position:absolute;left:0;top:1200px;width:1200px;height:589px;background:var(--soft)}
.advice{position:absolute;top:1438px;width:192px;height:276px;background:var(--white)}
.advice h4{font-size:12.5px;line-height:20px;font-weight:700;padding:25px 24px 0}
.advice p{font-size:11px;line-height:17px;color:var(--muted);padding:11px 24px 0}
.advice-photo{position:absolute;left:0;top:153px;width:192px;height:115px}

.video{position:absolute;left:163px;top:2049px;width:497px;height:367px;background:linear-gradient(135deg,#3f4a46 0%,#7d8a84 40%,#b9a89a 70%,#5a5e62 100%)}
.play{position:absolute;left:209px;top:144px;width:78px;height:78px;border-radius:50%;background:var(--teal);display:flex;align-items:center;justify-content:center}
.trust-title{position:absolute;left:763px;top:2068px;font-size:33px;line-height:47px;font-weight:700}
.trust-text{position:absolute;left:763px;top:2171px;width:280px;font-size:11px;line-height:17px;color:var(--muted)}
.feature{position:absolute;left:763px;width:280px}
.feature-title{position:absolute;left:42px;top:0;font-size:12.5px;line-height:20px;font-weight:700;width:240px}
.feature-sub{position:absolute;left:42px;top:43px;font-size:11px;color:var(--muted)}

.clients{position:absolute;left:5px;top:2532px;width:1195px;height:161px;background:var(--soft)}
.client{position:absolute;top:2585px;width:150px;text-align:center;font-size:30px;font-weight:700;color:#737373}

.newsletter{position:absolute;left:5px;top:2693px;width:1195px;height:120px;background:var(--navy-deep)}
.newsletter h3{position:absolute;left:231px;top:31px;font-size:20px;line-height:27px;font-weight:700;color:var(--white)}
.field{position:absolute;left:595px;top:34px;width:278px;height:47px;background:#f9f9f9;border:1px solid var(--line);border-radius:5px 0 0 5px;font-size:12px;color:var(--muted);padding:16px 16px}
.field-btn{position:absolute;left:873px;top:34px;width:97px;height:47px;background:var(--orange);border-radius:0 5px 5px 0;color:var(--white);font-size:12px;display:flex;align-items:center;justify-content:center}

.touch-band{position:absolute;left:0;top:2813px;width:1200px;height:670px;background:var(--soft)}
.contact{position:absolute;width:274px;text-align:center;background:var(--white)}
.contact .mail{font-size:12px;line-height:20px;font-weight:600;color:var(--navy)}
.contact .label{font-size:13px;font-weight:700;margin-top:13px}
.contact .req{margin:14px auto 0;width:133px;height:36px;border:1px solid var(--orange);border-radius:5px;color:var(--orange);font-size:12px;font-weight:600;display:flex;align-items:center;justify-content:center}
.contact.featured{background:var(--navy);color:var(--white)}
.contact.featured .mail{color:var(--white)}
.contact.featured .req{border-color:var(--white);color:var(--white)}

.cta-title{position:absolute;left:163px;top:3520px;font-size:21px;font-weight:700}
.cta-sub{position:absolute;left:163px;top:3556px;font-size:12px;color:var(--muted)}
.cta-btn{position:absolute;left:872px;top:3521px;width:133px;height:47px;background:var(--orange);color:var(--white);font-size:12px;font-weight:700;border-radius:5px;display:flex;align-items:center;justify-content:center}

.footer{position:absolute;left:0;top:3604px;width:1200px;height:226px;background:var(--navy-deep);color:var(--white)}
.fcol{position:absolute;top:42px}
.fcol h5{font-size:13px;font-weight:700;margin-bottom:20px}
.fcol li{list-style:none;font-size:12px;font-weight:500;line-height:29px}
.fcontact li{display:flex;align-items:center;gap:10px;line-height:33px}
.bottom{position:absolute;left:163px;top:3853px;font-size:12px;font-weight:500;color:var(--muted)}
.social{position:absolute;left:860px;top:3853px;display:flex;gap:14px;font-size:11px;font-weight:700;color:var(--teal)}
</style>
</head>
<body>

<section class="hero">
  <div class="hero-photo" role="img" aria-label="Photo of two colleagues smiling at a laptop screen in a bright office"></div>
  <div class="brand"><span class="brand-mark"></span><span class="brand-name">KEYSTONE ALLIES</span></div>
  <nav class="nav"><span>Home</span><span>Product</span><span>Pricing</span><span>Contact</span></nav>
  <svg class="menu-toggle" width="20" height="14" viewBox="0 0 20 14"><g stroke="#252b42" stroke-width="2" stroke-linecap="round"><line x1="1" y1="1" x2="19" y2="1"/><line x1="6" y1="7" x2="19" y2="7"/><line x1="11" y1="13" x2="19" y2="13"/></g></svg>
  <h1 class="hero-title">Staff Augmentation<br>and Operation<br>Support</h1>
  <p class="hero-text">We know how large objects will act,<br>but things on a small scale.</p>
  <div class="abs btn btn-primary" style="left:163px;top:455px;width:154px;height:41px">Get Quote Now</div>
  <div class="abs btn btn-ghost" style="left:326px;top:455px;width:128px;height:41px">Learn More</div>
</section>

<article class="service" style="left:163px">
  <svg width="40" height="34" viewBox="0 0 40 34" fill="none" stroke="#125e67" stroke-width="2.5"><rect x="2" y="8" width="36" height="24"/><path d="M13 8V2h14v6M2 17h36M16 14h8v6h-8z"/></svg>
  <h3>Environmental<br>Consulting</h3>
  <p>We focus on ergonomics and<br>meeting you where you work.</p>
</article>
<article class="service" style="left:462px">
  <svg width="40" height="38" viewBox="0 0 40 38" fill="none" stroke="#125e67" stroke-width="2.5"><rect x="4" y="2" width="32" height="8"/><path d="M4 10v26h32V10M4 16h32M14 36V24h12v12"/></svg>
  <h3>Finance and<br>consultancy</h3>
  <p>Just type what's on your mind<br>and we'll get you there.</p>
</article>
<article class="service featured" style="left:761px">
  <svg width="40" height="32" viewBox="0 0 40 32" fill="none" stroke="#ffffff" stroke-width="2.5"><rect x="2" y="2" width="36" height="28"/><path d="M20 2v28M25 10h8M25 16h8M25 22h8"/></svg>
  <h3>Financial Services<br>Consulting</h3>
  <p>the quick fox jumps over the<br>lazy dog</p>
</article>

<h2 class="abs center section-title" style="top:880px">Designing Better Experience</h2>
<p class="abs center section-sub" style="top:933px">Problems trying to resolve the conflict between the two major realms<br>of Classical physics: Newtonian mechanics</p>

<div class="stat" style="left:163px">
  <svg width="42" height="38" viewBox="0 0 42 38" fill="none" stroke="#125e67" stroke-width="2.5"><circle cx="21" cy="10" r="6"/><path d="M11 36v-6a10 10 0 0 1 20 0v6z"/><circle cx="8" cy="12" r="4"/><circle cx="34" cy="12" r="4"/><path d="M2 28a6 6 0 0 1 7-6M40 28a6 6 0 0 0-7-6"/></svg>
  <div class="stat-num">972 +</div><div class="stat-label">Consumer Products</div>
</div>
<div class="stat" style="left:387px">
  <svg width="42" height="38" viewBox="0 0 42 38" fill="none" stroke="#125e67" stroke-width="3" stroke-linecap="round"><path d="M4 24l9-9 8 10 8-12 9 8"/><g fill="#125e67"><circle cx="13" cy="15" r="3"/><circle cx="29" cy="13" r="3"/></g></svg>
  <div class="stat-num">181 +</div><div class="stat-label">Financial Services</div>
</div>
<div class="stat" style="left:612px">
  <svg width="42" height="38" viewBox="0 0 42 38" fill="none" stroke="#125e67" stroke-width="3"><circle cx="21" cy="13" r="10"/><circle cx="21" cy="13" r="4"/><path d="M14 21l-3 15 10-5 10 5-3-15"/></svg>
  <div class="stat-num">98%</div><div class="stat-label">Environmental</div>
</div>
<div class="stat" style="left:836px">
  <svg width="42" height="38" viewBox="0 0 42 38" fill="none" stroke="#125e67" stroke-width="2.5"><rect x="3" y="9" width="36" height="26"/><path d="M14 9V3h14v6M3 19h36M17 16h8v6h-8z"/></svg>
  <div class="stat-num">746 +</div><div class="stat-label">Business &amp; Finance</div>
</div>

<div class="advice-band"></div>
<h2 class="abs center section-title" style="top:1315px">Practice Advice</h2>
<p class="abs center section-sub" style="top:1368px">Problems trying to resolve the conflict between<br>the two major realms of Classical physics: Newtonian mechanics</p>

<article class="advice" style="left:168px">
  <h4>A single source<br>of truth</h4>
  <p>Newton thought that<br>light was made up of<br>particles.</p>
  <div class="advice-photo" role="img" aria-label="Photo of a coffee and laptop on a café table" style="background:linear-gradient(135deg,#6f8f7a,#c7b49a 60%,#3e4b4d)"></div>
</article>
<article class="advice" style="left:390px">
  <h4>Fastest way to<br>organize</h4>
  <p>“Quantum mechanics”<br>is the description of the<br>behaviour of matter</p>
  <div class="advice-photo" role="img" aria-label="Photo of glass office towers seen from below" style="background:linear-gradient(160deg,#a9b6c2,#3b4754 55%,#1e252d)"></div>
</article>
<article class="advice" style="left:614px">
  <h4>Fastest way to<br>take action</h4>
  <p>They describe a<br>universe consisting of<br>bodies moving</p>
  <div class="advice-photo" role="img" aria-label="Photo of hands reviewing papers beside a laptop" style="background:linear-gradient(135deg,#7a8d8c,#d6d9d4 50%,#4b5a5e)"></div>
</article>
<article class="advice" style="left:839px">
  <h4>Work better<br>together</h4>
  <p>They finally obtained<br>a consistent description<br>of the behaviour</p>
  <div class="advice-photo" role="img" aria-label="Black and white photo of people standing by large office windows" style="background:linear-gradient(135deg,#2a2a2a,#9a9a9a 50%,#3a3a3a)"></div>
</article>

<h2 class="abs center section-title" style="top:1877px">Who We Are</h2>
<p class="abs center section-sub" style="top:1932px">Problems trying to resolve the conflict between the two major realms<br>of Classical physics: Newtonian mechanics</p>

<div class="video" role="img" aria-label="Video still of two colleagues talking at a desk with a laptop">
  <div class="play"><svg width="22" height="24" viewBox="0 0 22 24"><path d="M2 1l19 11L2 23z" fill="#ffffff"/></svg></div>
</div>
<h2 class="trust-title">Most trusted in<br>our field</h2>
<p class="trust-text">Most calendars are designed for teams. Slate is designed for freelancers who want a simple way to plan their schedule.</p>
<div class="feature" style="top:2263px">
  <svg width="28" height="28" viewBox="0 0 28 28" fill="none" stroke="#ff7b3e" stroke-width="1.8"><circle cx="14" cy="8" r="4"/><circle cx="5" cy="10" r="3"/><circle cx="23" cy="10" r="3"/><path d="M7 26v-6a7 7 0 0 1 14 0v6M1 22a5 5 0 0 1 4-6M27 22a5 5 0 0 0-4-6"/></svg>
  <div class="feature-title">the quick fox jumps over the lazy dog</div>
  <div class="feature-sub">Things on a very small scale ...</div>
</div>
<div class="feature" style="top:2352px">
  <svg width="28" height="28" viewBox="0 0 28 28" fill="none" stroke="#ff7b3e" stroke-width="2" stroke-linecap="round"><path d="M4 22a11 11 0 1 1 20 0z"/><path d="M14 17l6-7"/></svg>
  <div class="feature-title">the quick fox jumps over the lazy dog</div>
  <div class="feature-sub">Things on a very small scale ...</div>
</div>

<div class="clients"></div>
<div class="client" style="left:156px">Norvik</div>
<div class="client" style="left:304px">Lumo</div>
<div class="client" style="left:454px">Quillan</div>
<div class="client" style="left:605px">Strata</div>
<div class="client" style="left:756px">Arcus</div>
<div class="client" style="left:907px">Orbly</div>

<section class="newsletter">
  <h3>Subscribe For Latest<br>Newsletter</h3>
  <div class="field">Your Email</div>
  <div class="field-btn">Subscribe</div>
</section>

<div class="touch-band"></div>
<h2 class="abs center section-title" style="top:2884px">Get In Touch</h2>
<p class="abs center section-sub" style="top:2936px">Problems trying to resolve the conflict between<br>the two major realms of Classical physics: Newtonian mechanics</p>

<div class="contact" style="left:189px;top:3060px;height:276px;padding-top:46px">
  <svg width="60" height="60" viewBox="0 0 60 60" fill="none" stroke="#125e67" stroke-width="4.5" stroke-linejoin="round"><path d="M12 4l10 14-6 6c4 8 12 16 20 20l6-6 14 10-6 8C30 58 2 30 4 10z"/><path d="M36 6a20 20 0 0 1 18 18M36 16a10 10 0 0 1 8 8"/></svg>
  <div class="mail" style="margin-top:12px">mara.lind@example.com<br>mara.lind@keystone.co</div>
  <div class="label">Get Support</div>
  <div class="req">Submit Request</div>
</div>
<div class="contact featured" style="left:462px;top:3036px;height:326px;padding-top:70px">
  <svg width="60" height="60" viewBox="0 0 60 60" fill="none" stroke="#ffffff" stroke-width="4.5"><path d="M30 57S10 36 10 22a20 20 0 0 1 40 0c0 14-20 35-20 35z"/><circle cx="30" cy="22" r="8"/></svg>
  <div class="mail" style="margin-top:12px">mara.lind@example.com<br>mara.lind@keystone.co</div>
  <div class="label">Get Support</div>
  <div class="req">Submit Request</div>
</div>
<div class="contact" style="left:736px;top:3060px;height:276px;padding-top:46px">
  <svg width="60" height="60" viewBox="0 0 60 60" fill="none" stroke="#125e67" stroke-width="4.5" stroke-linejoin="round"><path d="M56 4L4 26l22 8 8 22z"/><path d="M56 4L26 34"/></svg>
  <div class="mail" style="margin-top:12px">mara.lind@example.com<br>mara.lind@keystone.co</div>
  <div class="label">Get Support</div>
  <div class="req">Submit Request</div>
</div>

<h3 class="cta-title">Consulting Agency For Your Business</h3>
<p class="cta-sub">the quick fox jumps over the lazy dog</p>
<div class="cta-btn">Contact Us</div>

<footer class="footer">
  <div class="fcol" style="left:163px"><h5>Company Info</h5><ul><li>About Us</li><li>Carrier</li><li>We are hiring</li><li>Blog</li></ul></div>
  <div class="fcol" style="left:311px"><h5>Legal</h5><ul><li>About Us</li><li>Carrier</li><li>We are hiring</li><li>Blog</li></ul></div>
  <div class="fcol" style="left:462px"><h5>Features</h5><ul><li>Business Marketing</li><li>User Analytic</li><li>Live Chat</li><li>Unlimited Support</li></ul></div>
  <div class="fcol" style="left:610px"><h5>Resources</h5><ul><li>IOS &amp; Android</li><li>Watch a Demo</li><li>Customers</li><li>API</li></ul></div>
  <div class="fcol fcontact" style="left:763px"><h5>Get In Touch</h5><ul>
    <li><svg width="20" height="20" viewBox="0 0 20 20" fill="none" stroke="#8ec5f0" stroke-width="1.6"><path d="M4 1l3 5-2 2c1 3 4 6 7 7l2-2 5 3-2 3C8 19 1 12 2 3z"/></svg>(480) 555-0187</li>
    <li><svg width="20" height="22" viewBox="0 0 20 22" fill="none" stroke="#8ec5f0" stroke-width="1.6"><path d="M10 21S3 13 3 8a7 7 0 0 1 14 0c0 5-7 13-7 13z"/><circle cx="10" cy="8" r="3"/></svg>2290 Alder Ave.</li>
    <li><svg width="20" height="20" viewBox="0 0 20 20" fill="none" stroke="#8ec5f0" stroke-width="1.6" stroke-linejoin="round"><path d="M19 1L1 9l8 2 2 8z"/></svg>ines.varo@example.com</li>
  </ul></div>
</footer>

<p class="bottom">Made With Love &nbsp;All Right Reserved</p>
<div class="social"><span>Linkup</span><span>Pixly</span><span>Chirpr</span><span>Vidora</span></div>

</body>
</html>
```